***Design a Nutritional Supplement Label for Fernbrook Market!***

I have an existing label, I want to keep the logo but change the rest of the design. I am open to different creative ideas, but it needs to look appropriate for the shelves at Fernbrook Market. This means it needs to look professional and premium, without being sterile and boring. I feel like my current label looks a little 1990s. You can play with the colors, font and design elements, while keeping the logo, descriptive text and the same layout. Feel free to take some bold chances. (You cannot change the font in the supplement facts section)

Font styles to use
Sans Serif

Colors

Designer to choose colors to be used in the design.

Requirements
Must have
• Keep the same text and layout. Keep the "Spasm Shield" logo as-is. DO NOT CHANGE THE LOGO!!

```html
<!DOCTYPE html>
<html lang="en">
<head>
<meta charset="utf-8">
<title>Spasm Shield – Supplement Label</title>
<link rel="stylesheet" href="https://fonts.googleapis.com/css2?family=Josefin+Sans:wght@400;600&display=swap">
<style>
  :root {
    --page-bg: #f2f2f2;
    --label-bg: #ffffff;
    --brand-blue: #234a8a;
    --ink-blue: #1f3f7a;
    --photo-dark: #bdbdbd;
    --photo-light: #e2e2e2;
    --claim-ink: #f7f7f7;
  }
  * { margin: 0; padding: 0; box-sizing: border-box; }
  html, body {
    width: 1200px; height: 900px; overflow: hidden;
    background: var(--page-bg);
    font-family: "Josefin Sans", sans-serif;
  }
  .label {
    position: absolute; left: 271px; top: 32px;
    width: 657px; height: 836px;
    background: var(--label-bg);
    box-shadow: 0 2px 14px rgba(0,0,0,0.06);
    overflow: hidden;
  }
  .brand-panel {
    position: absolute; left: 255px; top: 32px;
    width: 402px; height: 561px;
    background: var(--brand-blue);
  }
  .wordmark {
    position: absolute; left: 0; width: 100%; top: 250px;
    text-align: center; color: #ffffff; font-weight: 600;
  }
  .wordmark-main { display: block; font-size: 60px; line-height: 1; letter-spacing: 0.01em; }
  .wordmark-sub { display: block; font-size: 24px; letter-spacing: 0.5em; margin-top: 8px; padding-left: 0.5em; }
  .count-block {
    position: absolute; left: 0; top: 128px; width: 240px;
    text-align: center; color: var(--ink-blue);
  }
  .count-number { font-size: 42px; line-height: 1; letter-spacing: 0.06em; }
  .count-unit { font-size: 22px; letter-spacing: 0.12em; margin-top: 4px; }
  .divider {
    position: absolute; left: 0; top: 218px; width: 253px; height: 6px;
    background: var(--ink-blue);
  }
  .product-type {
    position: absolute; left: 0; top: 248px; width: 240px;
    text-align: center; color: var(--ink-blue);
    font-size: 22px; line-height: 30px; letter-spacing: 0.12em;
  }
  .lifestyle-photo {
    position: absolute; left: 0; top: 403px; width: 536px; height: 315px;
    background: linear-gradient(90deg, var(--photo-dark) 0%, #d0d0d0 45%, var(--photo-light) 100%);
  }
  .claims {
    position: absolute; left: 462px; top: 416px; height: 290px;
    writing-mode: vertical-rl;
    color: var(--claim-ink);
    font-size: 22px; line-height: 30px; letter-spacing: 0.14em;
  }
</style>
</head>
<body>
  <main class="label">
    <div class="count-block">
      <div class="count-number">180</div>
      <div class="count-unit">CAPSULES</div>
    </div>
    <div class="divider"></div>
    <div class="product-type">DIETARY<br>SUPPLEMENT</div>

    <section class="brand-panel">
      <h1 class="wordmark">
        <span class="wordmark-main">SPASM</span>
        <span class="wordmark-sub">SHIELD</span>
      </h1>
    </section>

    <div class="lifestyle-photo" role="img" aria-label="Black and white photo of hands massaging a cramped leg muscle"></div>
    <p class="claims">HIGH ABSORBTION<br>FAST ACTING</p>
  </main>
</body>
</html>
```